依頼詳細
【ターゲット】
<今後>
30~40代 女性
会社員 主婦

◆サイトマップ
1.TOP
∟2.Concept
∟3.Staff(一覧)
∟4.Staff(詳細)
∟5.Menu
∟6.Shampoo/Treatment/Head spa
∟7.organic menu
∟8.Salon Gallery
∟9.News(一覧)
∟10.News(詳細)
∟11.Blog(一覧)
∟12.Blog(詳細)
∟13.Salon info
∟14.Recruit(求職者の皆様へ)
∟15.スタイリスト、アシスタント、理容師求人情報
∟16.アイリスト、ネイリスト求人情報
∟17.Q&A
∟18.Voice
∟19.Coupon
∟20.Contact
※TOPページへ、フローティングでついてくる予約アイコンを設けて頂きたいです。
※インスタも埋め込みをしたいので、そのスペースを設けて頂けると幸いです。

◆上記サイトマップについて
・グローバルメニューは
Concept、Staff、Menu、Blog、Salon info、Recruit、Contact
上記の項目を必須で組み込んでください。

◆参考にしたいサイト
http://temuro518.com/(このサイトの雰囲気にもうちょっとナチュラル感をプラスしたいです。)
http://www.salon-kuvela.jp/(このサイトくらいのフェミニン感が欲しいです。)
http://www.dompaseti.com/voice(フローティングでついてくる予約アイコンの参考)

◆現行サイト
http://tresmode-pk.com/

◆ミナトノート
https://beauty.minatonote.jp/slnH000472815/

※ワークブリッジの規約にもありますが、通常業務に支障が出る為
直接電話等のお問い合わせをお控え頂けますよう、ご協力の程お願い致します。
ご不明点等ありましたら、ワークブリッジ内メッセージで頂戴できますと幸いです。
シンプル 複雑
単色 カラフル
暗い 明るい
日常 高級
遊び心 厳粛
未来的 伝統的
女性的 男性的
茶系、グレー系、現在のHPへ使用しているカラーをそのまま引き継ぐ形でデザインをお願いいたします。
【素材について】

◆サロンの写真をダウンロードできるURLを下記に記載いたしますので、
ダウンロードしてご使用ください。
【ダウンロードURL:https://15.filevessel.nu/1201-q83ab2917c06dfe2874093815b27461d3

◆今回、ピクセルノ「https://jp.pixelno.com/」というサイトにて
制作中の間定期契約を致しました。デザインの際には、一度仮素材にて配置を頂き、ピクセルノ以外の素材は無料の物をご使用頂きたいです。
画像に番号が割り振られていますので、その番号をお教え頂ければ
こちらで正規データをダウンロード致します。
(画像の利用はマンスリーパック内でお願いいたします。)
お世話になっております。
提案数が芳しくないため、
期間を延長させて頂きます。
どうぞ自由な発想でご提案ください。
お世話になっております。
この度はご提案を頂きましてありがとうございます。

デザインの選定に時間がかかっておりますので、
選定期限を12月22日までに延長させて頂きます。

宜しくお願いいたします。

サロンの雰囲気に合っているため

この度はご提案を頂きありがとうございます。
またの機会がありましたら、よろしくおねがいいたします。

```html
<!DOCTYPE html>
<html lang="ja">
<head>
<meta charset="utf-8">
<title>NOELLE hair salon</title>
<link href="https://fonts.googleapis.com/css2?family=Cormorant+Garamond:wght@400;500;600&family=Noto+Sans+JP:wght@300;400;500&display=swap" rel="stylesheet">
<style>
:root{
  --ink:#333;
  --sub:#777;
  --line:#bdb8b4;
  --band:#d7d3cf;
  --tile:#dcdcdc;
  --white:#fff;
  --footer:#141414;
  --light:#ddd;
}
*{margin:0;padding:0;box-sizing:border-box}
html,body{width:1200px;height:4258px;overflow:hidden;background:var(--white)}
body{position:relative;font-family:"Noto Sans JP",sans-serif;color:var(--ink)}
.abs{position:absolute}

.brand-mark{left:560px;top:24px;width:80px;height:80px;border:1px solid #999;border-radius:50%}
.brand-name{left:0;top:114px;width:1200px;text-align:center;font-family:"Cormorant Garamond",serif;font-size:15px;letter-spacing:4px;color:var(--ink)}
.gnav{left:0;top:220px;width:1200px;display:flex;justify-content:center;gap:44px;font-family:"Cormorant Garamond",serif;font-size:17px;font-weight:500}
.gnav span::before{content:"•";margin-right:8px;font-size:12px;color:var(--sub)}

.hero{left:0;top:280px;width:1200px;height:448px;background:linear-gradient(120deg,#eef2f4 0%,#dde5e9 40%,#c9d3d8 70%,#e9eef0 100%)}

.reserve{left:1000px;top:732px;width:176px;height:176px;border-radius:50%;background:#f4f7ee;border:2px solid #b8cc9a;display:flex;flex-direction:column;align-items:center;justify-content:center;font-family:"Cormorant Garamond",serif}
.reserve b{font-size:17px;font-weight:600}
.reserve i{font-style:normal;font-size:11px;color:var(--sub);margin-top:4px;letter-spacing:1px}

.concept-photo{left:120px;top:848px;width:330px;height:320px;background:linear-gradient(90deg,#6b5a4c,#cdbfae 50%,#eee8e0)}
.concept-head{left:500px;top:1000px;width:560px;font-size:16px;line-height:1.9;letter-spacing:1px}
.concept-body{left:500px;top:1090px;width:540px;font-size:11px;line-height:2;color:#555}

.band{left:0;width:1200px;background:var(--band)}
.title{left:0;width:1200px;text-align:center;font-family:"Cormorant Garamond",serif;font-size:30px;font-weight:600}
.title::after{content:"";display:block;width:28px;height:2px;background:var(--ink);margin:10px auto 0}

.gallery-photo{top:1420px;width:180px;height:180px}

.staff-photo{top:1780px;width:216px;height:216px;border-radius:50%}
.staff-name{top:2012px;width:216px;text-align:center}
.staff-name small{display:block;font-family:"Cormorant Garamond",serif;font-size:10px;color:var(--sub);letter-spacing:1px}
.staff-name span{font-size:12px}

.blog-row{left:120px;width:960px;height:60px;border-bottom:1px solid var(--line);display:flex;align-items:center;font-size:14px}
.blog-row .date{width:380px;padding-left:90px}
.blog-row .post{text-decoration:underline}

.more{left:490px;width:220px;height:36px;border:1px solid var(--ink);background:var(--white);display:flex;align-items:center;justify-content:center;gap:40px;font-size:13px}

.photolog-tile{width:148px;height:148px;background:var(--tile)}

.map{left:0;top:3248px;width:1200px;height:272px;background:linear-gradient(135deg,#ece8e0,#f4f1ea 40%,#e4e7ea 70%,#efece6)}

.info-col{top:3560px;width:300px;text-align:center;font-size:11px;line-height:1.9;color:#444}
.info-col h3{font-family:"Cormorant Garamond",serif;font-size:17px;font-weight:600;margin-bottom:10px;color:var(--ink)}

.footer{left:0;top:3880px;width:1200px;height:378px;background:var(--footer);color:var(--light)}
.footer .brand-mark{top:30px;border-color:#aaa;width:70px;height:70px;left:565px}
.footer .brand-name{top:110px;color:var(--light);font-size:13px}
.footer .gnav{top:160px;font-size:13px;font-family:"Noto Sans JP",sans-serif;gap:40px;color:var(--light)}
.footer .gnav span::before{color:#999}
.fcol{top:210px;width:260px;text-align:center;font-size:11px;line-height:1.8}
.fcol h4{font-size:11px;font-weight:500;margin-bottom:4px;color:#fff}
.follow{left:880px;top:210px;width:160px;text-align:center;font-size:11px}
.follow div{display:flex;justify-content:center;gap:14px;margin-top:10px}
.follow span{display:flex;align-items:center;gap:5px;font-size:11px}
.follow span::before{content:"";width:10px;height:10px;background:var(--light)}
</style>
</head>
<body>

<header>
  <div class="abs brand-mark"></div>
  <div class="abs brand-name">NOELLE</div>
  <nav class="abs gnav">
    <span>Concept</span><span>Staff</span><span>Menu</span><span>Blog</span><span>Salon info</span><span>Recruit</span><span>Contact</span>
  </nav>
</header>

<div class="abs hero" role="img" aria-label="白い布に刺繍されたサロン名のイメージ写真"></div>

<div class="abs reserve"><b>Reservation</b><i>ご予約はこちら</i></div>

<section class="concept">
  <div class="abs concept-photo" role="img" aria-label="木目と白を基調にしたサロン店内の写真"></div>
  <p class="abs concept-head">老舗に負けない、<br>100年後も引き継がれる仕事をする美容室にする</p>
  <p class="abs concept-body">お客様一人ひとりと丁寧に向き合う時間を大切にしています。落ち着いた空間でゆったりとお過ごしいただき、毎日のスタイリングが少し楽しくなる、そんな髪型をご提案いたします。</p>
</section>

<section>
  <div class="abs band" style="top:1292px;height:340px"></div>
  <h2 class="abs title" style="top:1318px">Gallery</h2>
  <div class="abs gallery-photo" style="left:120px;background:linear-gradient(135deg,#3d3a38,#cfc6bd)" role="img" aria-label="メンズショートスタイルの写真"></div>
  <div class="abs gallery-photo" style="left:380px;background:linear-gradient(135deg,#7a5a45,#e2d6c8)" role="img" aria-label="ショートボブスタイルの写真"></div>
  <div class="abs gallery-photo" style="left:640px;background:linear-gradient(135deg,#9c4a3a,#d7bfb0)" role="img" aria-label="レッド系カラースタイルの写真"></div>
  <div class="abs gallery-photo" style="left:900px;background:linear-gradient(135deg,#8c7058,#e6ddd3)" role="img" aria-label="ボブスタイルの写真"></div>
</section>

<section>
  <h2 class="abs title" style="top:1692px">Staff</h2>
  <div class="abs staff-photo" style="left:320px;background:linear-gradient(160deg,#e7e4e0,#8d8782)" role="img" aria-label="スタイリストのポートレート"></div>
  <div class="abs staff-photo" style="left:672px;background:linear-gradient(160deg,#dfe3e6,#7d848a)" role="img" aria-label="スタイリストのポートレート"></div>
  <div class="abs staff-name" style="left:320px"><small>STYLIST</small><span>村瀬 和真</span></div>
  <div class="abs staff-name" style="left:672px"><small>STYLIST</small><span>高野 俊介</span></div>
</section>

<section>
  <div class="abs band" style="top:2088px;height:464px"></div>
  <h2 class="abs title" style="top:2122px">Blog</h2>
  <div class="abs blog-row" style="top:2218px"><span class="date">2018.05.09</span><span class="post">2415 MELLOWDAY スープ</span></div>
  <div class="abs blog-row" style="top:2278px"><span class="date">2018.05.09</span><span class="post">2415 MELLOWDAY スープ</span></div>
  <div class="abs blog-row" style="top:2338px"><span class="date">2018.05.09</span><span class="post">2415 MELLOWDAY スープ</span></div>
  <div class="abs more" style="top:2466px"><span>more</span><span>›</span></div>
</section>

<section>
  <h2 class="abs title" style="top:2574px">Photolog</h2>
  <div class="abs photolog-tile" style="left:264px;top:2672px"></div>
  <div class="abs photolog-tile" style="left:440px;top:2672px"></div>
  <div class="abs photolog-tile" style="left:614px;top:2672px"></div>
  <div class="abs photolog-tile" style="left:788px;top:2672px"></div>
  <div class="abs photolog-tile" style="left:264px;top:2850px"></div>
  <div class="abs photolog-tile" style="left:440px;top:2850px"></div>
  <div class="abs photolog-tile" style="left:614px;top:2850px"></div>
  <div class="abs photolog-tile" style="left:788px;top:2850px"></div>
  <div class="abs more" style="top:3066px"><span>more</span><span>›</span></div>
</section>

<section>
  <h2 class="abs title" style="top:3160px">Shop Info</h2>
  <div class="abs map" role="img" aria-label="サロン周辺の地図"></div>
  <div class="abs info-col" style="left:120px">
    <h3>Access</h3>
    <p>〒107-0062 東京都港区南青山 0-0-0 ルミエ2F</p>
    <p>南青山駅 A2出口より徒歩3分</p>
    <p>大通り沿いの白い建物の2階です</p>
    <p>お車の方は近隣のパーキングをご利用ください</p>
  </div>
  <div class="abs info-col" style="left:450px">
    <h3>Contact</h3>
    <p>ご予約・お問い合わせはお電話または</p>
    <p>予約フォームよりお気軽にどうぞ</p>
    <p>03-0000-0000</p>
    <p>ネット予約はこちら</p>
  </div>
  <div class="abs info-col" style="left:780px">
    <h3>Open</h3>
    <p>火〜金　11:00 〜 21:00</p>
    <p>土　10:00 〜 20:00</p>
    <p>日・祝　10:00 〜 19:00</p>
    <p>定休日　毎週月曜日</p>
  </div>
</section>

<footer class="abs footer">
  <div class="abs brand-mark"></div>
  <div class="abs brand-name">NOELLE</div>
  <nav class="abs gnav">
    <span>Concept</span><span>Menu</span><span>Staff</span><span>Blog</span><span>Salon info</span><span>Contact</span><span>Recruit</span>
  </nav>
  <div class="abs fcol" style="left:160px"><h4>Address</h4><p>〒107-0062 東京都港区南青山 0-0-0</p><h4 style="margin-top:8px">Phone Number</h4><p>03-0000-0000</p></div>
  <div class="abs fcol" style="left:470px"><h4>Open</h4><p>火〜金　11:00 〜 21:00</p><p>土　10:00 〜 20:00</p><p>日・祝　10:00 〜 19:00</p><p>定休日　毎週月曜日</p></div>
  <div class="abs follow"><p>Follow us</p><div><span>Photolog</span><span>Facelink</span></div></div>
</footer>

</body>
</html>
```